The Lantern and Harbor: for Rosalind and Elias by Dorsey Valtane

I need an album cover design for a song dedicated to Elias and Rosalind Hale Barrow, in anticipation for EHB weekend. the main question the song raises is: when was the last time someone said that you can achieve greatness? In other words, we often do not live to our full potential. The design should be simple and clean, using a modern Sans Serif font. 1600 x 1600 pixels, best-quality RGB mode, and delivered as a JPEG.

Target Market(s)

young men and women, 18-35 years old

Font styles to use
Sans Serif

Colors
3277b5
34a7d7

Requirements
Must have
• Name of song (The Lantern and Harbor: for Rosalind and Elias) and artist (Dorsey Valtane)
Nice to have
• Something suggesting elegance without being overt or pretentious
Should not have
• Serif font, too many colors

```html
<!DOCTYPE html>
<html lang="en">
<head>
<meta charset="utf-8">
<title>The Lantern and Harbor — Dorsey Valtane</title>
<link rel="stylesheet" href="https://fonts.googleapis.com/css2?family=Belleza&family=Great+Vibes&display=swap">
<style>
  :root {
    --cover-centre: #0cb6ec;
    --cover-mid: #0aa2dd;
    --cover-edge: #0786c4;
    --title-blue: #1c5f99;
    --emblem-deep: #1f6aab;
    --emblem-light: #3a8fcf;
    --emblem-shadow: rgba(8, 60, 110, 0.28);
    --text-white: #ffffff;
  }
  * { margin: 0; padding: 0; box-sizing: border-box; }
  html, body {
    width: 1200px;
    height: 1200px;
    overflow: hidden;
  }
  .album-cover {
    position: relative;
    width: 1200px;
    height: 1200px;
    background: radial-gradient(circle at 50% 42%, var(--cover-centre) 0%, var(--cover-mid) 38%, var(--cover-edge) 100%);
    font-family: "Belleza", "Helvetica Neue", Arial, sans-serif;
    text-align: center;
  }
  .emblem {
    position: absolute;
    left: 480px;
    top: 210px;
    width: 400px;
    height: 380px;
  }
  .song-title {
    position: absolute;
    left: 0;
    width: 100%;
    top: 604px;
    font-size: 68px;
    font-weight: 400;
    color: var(--title-blue);
    letter-spacing: 0.5px;
    line-height: 1;
    white-space: nowrap;
  }
  .song-dedication {
    position: absolute;
    left: 0;
    width: 100%;
    top: 686px;
    font-size: 46px;
    font-weight: 400;
    color: var(--text-white);
    line-height: 1;
    white-space: nowrap;
  }
  .artist-name {
    position: absolute;
    left: 0;
    width: 100%;
    top: 1024px;
    font-family: "Great Vibes", "Brush Script MT", cursive;
    font-size: 58px;
    font-weight: 400;
    color: var(--text-white);
    line-height: 1;
    white-space: nowrap;
  }
</style>
</head>
<body>
  <main class="album-cover">
    <svg class="emblem" viewBox="0 0 400 380" role="img" aria-label="Emblem area reserved for the song's artwork mark">
      <defs>
        <linearGradient id="emblemFill" x1="0" y1="0" x2="0" y2="1">
          <stop offset="0" stop-color="var(--emblem-light)"/>
          <stop offset="1" stop-color="var(--emblem-deep)"/>
        </linearGradient>
        <radialGradient id="emblemShadow" cx="0.5" cy="0.5" r="0.5">
          <stop offset="0" stop-color="var(--emblem-shadow)"/>
          <stop offset="1" stop-color="rgba(8, 60, 110, 0)"/>
        </radialGradient>
      </defs>
      <rect x="6" y="10" width="380" height="330" rx="40" fill="url(#emblemFill)" opacity="0.55"/>
      <ellipse cx="190" cy="358" rx="170" ry="12" fill="url(#emblemShadow)"/>
    </svg>

    <h1 class="song-title">The Lantern and Harbor</h1>
    <p class="song-dedication">for ROSALIND and ELIAS</p>
    <p class="artist-name">Dorsey Valtane</p>
  </main>
</body>
</html>
```